Business cards Dör Kornhüüs GmbH & Co.KG

We need a uniform business card design template for our employees.
A template should be created to have the same design for all business cards.

Contact Information for Business Card

Firma und Firmierung, Name, Funktion in Unternehmen, Anschrift, Tel. Handynummer, Emailadresse, Internetseite

Colors

Designer to choose colors to be used in the design.

Requirements
Must have
• Our company logo must be on it

```html
<!DOCTYPE html>
<html lang="de">
<head>
<meta charset="utf-8">
<title>Dör Kornhüüs – Visitenkarte</title>
<link href="https://fonts.googleapis.com/css2?family=Montserrat:wght@500;800&family=Open+Sans:wght@400;600&display=swap" rel="stylesheet">
<style>
  :root {
    --page: #2b2927;
    --card-light: #733d33;
    --card-dark: #552c27;
    --pink: #f2808e;
    --lilac: #d7a8dc;
    --white: #ffffff;
    --muted: #b7a8a6;
  }
  * { box-sizing: border-box; margin: 0; padding: 0; }
  html, body { width: 1200px; height: 1200px; overflow: hidden; }
  body {
    background: var(--page);
    font-family: "Open Sans", sans-serif;
    position: relative;
  }
  .card {
    position: absolute;
    left: 150px;
    width: 900px;
    height: 514px;
    border-radius: 34px;
    background: radial-gradient(ellipse at 50% 45%, var(--card-light) 0%, var(--card-dark) 85%);
    overflow: hidden;
  }
  .card--front { top: 44px; }
  .card--back { top: 642px; }

  .wordmark {
    position: absolute;
    font-family: "Montserrat", sans-serif;
    font-weight: 500;
    color: var(--lilac);
    font-size: 60px;
    letter-spacing: 1px;
    white-space: nowrap;
    line-height: 1;
  }
  .card--front .wordmark { left: 0; right: 0; top: 170px; text-align: center; }
  .card--back .wordmark { right: 80px; top: 118px; font-size: 52px; }

  .url-row {
    position: absolute;
    left: 0; right: 0; top: 340px;
    display: flex;
    align-items: center;
    justify-content: center;
    gap: 18px;
  }
  .url-row__wedge { width: 190px; height: 22px; flex: none; }
  .web-url {
    font-family: "Montserrat", sans-serif;
    font-weight: 500;
    font-size: 30px;
    line-height: 1;
    color: var(--white);
    letter-spacing: 0.5px;
    white-space: nowrap;
  }

  .divider {
    position: absolute;
    left: 150px;
    top: 306px;
    width: 680px;
    height: 3px;
    background: var(--lilac);
  }

  .person {
    position: absolute;
    left: 150px;
    top: 216px;
  }
  .person__name {
    font-family: "Montserrat", sans-serif;
    font-weight: 800;
    font-size: 42px;
    color: var(--white);
    letter-spacing: 1px;
    line-height: 1;
  }
  .person__role {
    margin-top: 8px;
    font-size: 24px;
    line-height: 1.2;
    color: var(--muted);
  }

  .contacts {
    position: absolute;
    left: 150px;
    top: 322px;
    list-style: none;
  }
  .contacts li {
    display: flex;
    align-items: center;
    gap: 14px;
    font-size: 21px;
    color: var(--white);
    line-height: 1;
    height: 34px;
  }
  .contacts svg { width: 22px; height: 22px; flex: none; }
</style>
</head>
<body>

<section class="card card--front" aria-label="Visitenkarte Vorderseite">
  <div class="wordmark">Dör Kornhüüs</div>
  <div class="url-row">
    <svg class="url-row__wedge" viewBox="0 0 190 22" aria-hidden="true">
      <polygon points="0,22 190,0 190,22" fill="var(--pink)"/>
    </svg>
    <div class="web-url">WWW.WEBSITEHERE.COM</div>
    <svg class="url-row__wedge" viewBox="0 0 190 22" aria-hidden="true">
      <polygon points="0,0 190,0 0,22" fill="var(--pink)"/>
    </svg>
  </div>
</section>

<section class="card card--back" aria-label="Visitenkarte Rückseite">
  <div class="wordmark">Dör Kornhüüs</div>
  <div class="person">
    <div class="person__name">MIKE SMITH</div>
    <div class="person__role">Manager</div>
  </div>
  <div class="divider" aria-hidden="true"></div>
  <ul class="contacts">
    <li>
      <svg viewBox="0 0 24 24" aria-hidden="true"><rect x="6" y="2" width="12" height="20" rx="2" fill="none" stroke="var(--pink)" stroke-width="2"/><circle cx="12" cy="18.5" r="1" fill="var(--pink)"/></svg>
      +0000 -000- 0000
    </li>
    <li>
      <svg viewBox="0 0 24 24" aria-hidden="true"><path d="M6 3l4 4-2 3c1.5 3 3 4.5 6 6l3-2 4 4-3 3C10 20 4 14 3 6z" fill="var(--pink)"/></svg>
      +0000 -000- 0000
    </li>
    <li>
      <svg viewBox="0 0 24 24" aria-hidden="true"><rect x="2" y="5" width="20" height="14" fill="var(--pink)"/><path d="M2 5l10 8 10-8" fill="none" stroke="var(--card-dark)" stroke-width="1.5"/></svg>
      email@addresshere.com
    </li>
    <li>
      <svg viewBox="0 0 24 24" aria-hidden="true"><circle cx="12" cy="12" r="9" fill="none" stroke="var(--pink)" stroke-width="2"/><ellipse cx="12" cy="12" rx="4" ry="9" fill="none" stroke="var(--pink)" stroke-width="1.5"/><line x1="3" y1="12" x2="21" y2="12" stroke="var(--pink)" stroke-width="1.5"/></svg>
      www.websitehere.com
    </li>
  </ul>
</section>

</body>
</html>
```